K&T Smokehouse Website Design Project

K& T Smokehouse AsadorÃa is a fast-casual restaurant that specializes in southern culture, soul food, baby back ribs and bourbon whiskey.
We need a functional and user friendly website design for our customers to be able to explore our menu options, learn about our culture, as well as be able to place and pay for online orders that can be picked up at the nearest restaurant. Benchmarks for our website are www.velmorbakes.example, www.quarnito.example and www.surelapeak.example
The site design should also serve as an initial point of contact for prospective franchisees to dig and learn about the brand and business opportunity.
We want customers (consumers and potential franchisees) to be able to experience FIRST THE FOOD, but also the style and culture of our restaurants via the website design. Key elements for this are: soul food (Fill Every Plate), southern culture, friendly service, bluegrass/folk music, bourbon/moonshine/Tennessee whisky, modern butcher-shop design as well as industrial, wood, modern rustic, organic elements. (see restaurant images of tile, concrete, vintage scales, green wall, etc)
We want the website to provide a good overall brand image and also drive participation and sales by via images of our food, by these images being at front and center of the website design. See benchmark websites (Velmor, Surela Peak, Quarnito) for good examples of this.
Other elements to take under consideration for the website design are:
* Illustrative but simple menu
* Hacer un pedido (order online), Loyalty Program and Franquicias sections should have different, separate and easy to see buttons in the homepage.
* Simple, but modern functionality overall for the website.
* Respect colors and elements of the brand (attached some photos and examples)
* Brand Typography included (NAMES OF TYPOGRAPHY: BEBAS, SONGBIRD, CANTER & VAST SHADOW)
Minimum Deliverables: Home Page, Menu and Order Online. 3 pages total.
• More examples can be found at: www.facebook.com/ktsmokehouseasadoria
• Website architecture / Site Map ATTACHED
* More design elements attached.
* Screenshots of some good elements to take under consideration for website functionality and design.
- BEBAS, SONGBRID, CANTER & VAST SHADOW

```html
<!DOCTYPE html>
<html lang="en">
<head>
<meta charset="utf-8">
<title>K&amp;T Smokehouse — Home</title>
<link rel="stylesheet" href="https://fonts.googleapis.com/css2?family=Oswald:wght@300;400;600;700&family=PT+Serif&family=Roboto:wght@400;700&family=Roboto+Condensed:wght@700&display=swap">
<style>
:root{
  --black:#0b0b0b;
  --ink:#1a1a1a;
  --white:#ffffff;
  --red:#d3223d;
  --maroon:#6b1a30;
  --maroon-soft:rgba(110,26,52,.78);
  --grey:#9a9a9a;
  --rule:#dcdcdc;
  --dark:#141414;
  --gold:#c9a640;
}
*{box-sizing:border-box;margin:0;padding:0}
html,body{width:1200px;height:2878px;overflow:hidden;background:var(--white);font-family:"Roboto",Arial,sans-serif;color:var(--ink)}
.page{position:relative;width:1200px;height:2878px}

/* top utility bar */
.utility{position:absolute;top:0;left:0;width:1200px;height:29px;background:var(--black);color:var(--white);font-size:10px;display:flex;align-items:center;justify-content:space-between;padding:0 0 0 63px}
.utility .member{display:flex;gap:22px;letter-spacing:.5px}
.utility .social{display:flex;align-items:center;height:29px}
.utility .social-label{margin-right:14px;letter-spacing:.5px}
.utility .social-btn{width:30px;height:29px;border-left:1px solid #333;display:flex;align-items:center;justify-content:center}
.utility .social-btn span{width:10px;height:10px;background:#cfcfcf;border-radius:2px}

/* main nav */
.nav{position:absolute;top:29px;left:0;width:1200px;height:115px;background:var(--white)}
.brand{position:absolute;left:63px;top:22px;height:70px;display:flex;align-items:center;gap:12px}
.brand-dot{width:56px;height:56px;border-radius:50%;background:var(--black)}
.brand-name{font-family:"Oswald",sans-serif;font-weight:700;font-size:24px;color:var(--black);letter-spacing:.5px}
.menu{position:absolute;left:578px;top:0;height:115px;display:flex;font-family:"PT Serif",serif;font-size:17px;text-transform:uppercase;letter-spacing:.5px}
.menu a{color:#333;text-decoration:none;display:flex;align-items:center;padding:0 14px}
.menu a.active{background:var(--red);color:var(--white);padding:0 18px}

/* hero */
.hero{position:absolute;top:144px;left:0;width:1200px;height:593px;background:linear-gradient(180deg,#3b2a1c 0%,#7a4a26 38%,#4a2d1c 65%,#1c130d 100%)}
.hero-title{position:absolute;top:232px;width:100%;text-align:center;color:var(--white);font-family:"Oswald",sans-serif;font-weight:300;font-size:90px;line-height:90px;letter-spacing:1px}
.hero-sub{position:absolute;top:322px;width:100%;text-align:center;color:var(--white);font-size:23px;line-height:37px}
.hero-actions{position:absolute;top:397px;left:0;width:100%;display:flex;justify-content:center;gap:16px}
.btn-hero{width:222px;height:43px;color:var(--white);font-size:16px;display:flex;align-items:center;justify-content:center;letter-spacing:.5px;text-transform:uppercase}
.btn-order{background:var(--red)}
.btn-loyalty{background:var(--maroon)}
.btn-franchise{border:2px solid var(--white)}

/* feature */
.feature{position:absolute;top:737px;left:0;width:1200px;height:515px;background:var(--white)}
.feature-photo{position:absolute;right:0;top:0;width:515px;height:515px;background:linear-gradient(135deg,#e8e2dc 0%,#b4725a 45%,#8a4a35 70%,#dfe6d3 100%)}
.feature h2{position:absolute;left:63px;top:100px;font-family:"Oswald",sans-serif;font-weight:700;font-size:48px;line-height:54px;text-transform:uppercase;color:var(--black)}
.feature h3{position:absolute;left:63px;top:224px;width:590px;font-family:"Oswald",sans-serif;font-weight:400;font-size:28px;line-height:34px;color:var(--grey);border-top:1px solid var(--rule);padding-top:2px;text-transform:uppercase}
.feature p{position:absolute;left:63px;top:266px;width:610px;font-size:13.5px;line-height:19.5px;color:var(--black)}
.btn-reserve{position:absolute;left:63px;top:385px;width:150px;height:44px;border-radius:22px;background:var(--maroon);color:var(--white);font-family:"Oswald",sans-serif;font-weight:600;font-size:14px;display:flex;align-items:center;justify-content:center;text-transform:uppercase}

/* reviews */
.reviews{position:absolute;top:1252px;left:0;width:1200px;height:734px;background:var(--dark)}
.section-title{font-family:"Oswald",sans-serif;font-weight:700;font-size:46px;line-height:52px;text-transform:uppercase}
.reviews .section-title{position:absolute;left:63px;top:50px;color:var(--white)}
.carousel-arrows{position:absolute;left:1036px;top:95px;display:flex;gap:8px}
.carousel-arrows svg{width:36px;height:36px}
.review-card{position:absolute;top:193px;width:306px;color:var(--white)}
.review-photo{width:306px;height:247px}
.review-tag{margin-top:8px;height:18px;background:var(--white);color:var(--black);font-family:"Roboto Condensed",sans-serif;font-weight:700;font-size:13px;line-height:18px;text-transform:uppercase}
.review-text{margin-top:9px;font-size:13px;font-weight:700;line-height:17px}
.stars{margin-top:4px;display:flex;gap:3px}
.stars svg{width:14px;height:14px}
.reviewer{margin-top:40px;display:flex;align-items:center;gap:18px}
.avatar{width:84px;height:84px;border-radius:50%;background:#c9b49a;border:3px solid #2a2a2a}
.reviewer-name{font-size:14px;font-weight:700;line-height:18px}
.reviewer-place{font-size:13px;line-height:17px;color:#ddd}

/* browse */
.browse{position:absolute;top:1986px;left:0;width:1200px;height:849px;background:var(--white)}
.browse .section-title{position:absolute;left:63px;top:52px;color:var(--black)}
.browse-rule{position:absolute;left:63px;top:178px;width:1071px;height:1px;background:var(--rule)}
.category{position:absolute;width:513px;height:167px;overflow:hidden}
.category .photo{position:absolute;inset:0}
.category svg.band{position:absolute;inset:0;width:513px;height:167px}
.category .icon{position:absolute;right:40px;top:22px;width:58px;height:58px;border:3px solid var(--white);border-radius:50%}
.category .label{position:absolute;right:14px;bottom:8px;color:var(--white);font-family:"Roboto Condensed",sans-serif;font-weight:700;font-size:46px;line-height:54px;text-transform:uppercase;letter-spacing:-.5px}

/* footer */
.footer{position:absolute;top:2835px;left:0;width:1200px;height:43px;background:var(--black);color:var(--white);font-size:11px;display:flex;align-items:center;justify-content:space-between;padding:0 50px 0 63px;letter-spacing:.4px}
.footer nav{display:flex;gap:34px}
</style>
</head>
<body>
<div class="page">

  <div class="utility">
    <div class="member"><span>MEMBER LOGIN ▸</span><span>JOIN</span></div>
    <div class="social">
      <span class="social-label">SOCIAL :</span>
      <span class="social-btn"><span></span></span>
      <span class="social-btn"><span></span></span>
      <span class="social-btn"><span></span></span>
      <span class="social-btn"><span></span></span>
      <span class="social-btn"><span></span></span>
    </div>
  </div>

  <header class="nav">
    <div class="brand"><span class="brand-dot"></span><span class="brand-name">K&amp;T SMOKEHOUSE</span></div>
    <nav class="menu">
      <a class="active">Dine</a>
      <a>Browse</a>
      <a>Members</a>
      <a>Who We Are</a>
      <a>Stories</a>
    </nav>
  </header>

  <section class="hero" role="img" aria-label="Evening photo of a restaurant terrace with lanterns and wooden tables">
    <h1 class="hero-title">INCREDIBLE SERVICE</h1>
    <p class="hero-sub">Slow-smoked baby back ribs, soul food and a fine pour of bourbon.<br>Fill Every Plate. Pull Up a Chair. Stay for the Bluegrass.</p>
    <div class="hero-actions">
      <div class="btn-hero btn-order">&gt;&gt; Order Now</div>
      <div class="btn-hero btn-loyalty">Loyalty Program</div>
      <div class="btn-hero btn-franchise">Franchise With Us</div>
    </div>
  </section>

  <section class="feature">
    <h2>Announcing '14 Top Rated<br>Smokehouse</h2>
    <h3>The Rib Shack</h3>
    <p>Smoking low and slow for almost 30 years, K&amp;T Smokehouse has become a local landmark, famous for baby back ribs and southern soul food in a rustic, friendly butcher-shop setting.<br>Pair every plate with our bourbon and moonshine list, live folk and bluegrass on weekends, and pick up online orders at your nearest restaurant.</p>
    <div class="btn-reserve">Reserve Dinner</div>
    <div class="feature-photo" role="img" aria-label="Close-up photo of sliced smoked pork on a plate with greens"></div>
  </section>

  <section class="reviews">
    <h2 class="section-title">Latest User<br>Reviews</h2>
    <div class="carousel-arrows">
      <svg viewBox="0 0 36 36"><circle cx="18" cy="18" r="18" fill="#fff"/><path d="M11 15l7 7 7-7" fill="none" stroke="#111" stroke-width="3"/></svg>
      <svg viewBox="0 0 36 36"><circle cx="18" cy="18" r="18" fill="#fff"/><path d="M11 15l7 7 7-7" fill="none" stroke="#111" stroke-width="3"/></svg>
    </div>

    <article class="review-card" style="left:63px">
      <div class="review-photo" role="img" aria-label="Photo of a glazed rack of smoked ribs" style="background:linear-gradient(135deg,#3a3a3a,#c8643a 50%,#e7e0d4)"></div>
      <div class="review-tag">Ribs &amp; Bourbon</div>
      <p class="review-text">Fall-off-the-bone ribs at fair prices. Friendly service. My favorite smokehouse in the whole county. Consistently good."</p>
      <div class="stars"><svg viewBox="0 0 14 14"><path d="M7 0l2 5h5l-4 3 2 6-5-4-5 4 2-6-4-3h5z" fill="var(--gold)"/></svg><svg viewBox="0 0 14 14"><path d="M7 0l2 5h5l-4 3 2 6-5-4-5 4 2-6-4-3h5z" fill="var(--gold)"/></svg><svg viewBox="0 0 14 14"><path d="M7 0l2 5h5l-4 3 2 6-5-4-5 4 2-6-4-3h5z" fill="var(--gold)"/></svg><svg viewBox="0 0 14 14"><path d="M7 0l2 5h5l-4 3 2 6-5-4-5 4 2-6-4-3h5z" fill="var(--gold)"/></svg></div>
      <div class="reviewer"><div class="avatar" role="img" aria-label="Reviewer portrait"></div><div><div class="reviewer-name">Dana Whitfield</div><div class="reviewer-place">Binghamton , New York</div></div></div>
    </article>

    <article class="review-card" style="left:446px">
      <div class="review-photo" role="img" aria-label="Photo of a pulled pork sandwich on a wooden board" style="background:linear-gradient(135deg,#5a3a26,#b86a48 50%,#d9c4a4)"></div>
      <div class="review-tag">Soul Food Specials</div>
      <p class="review-text">Real southern comfort food. Warm, friendly staff and great bluegrass on Fridays. The cornbread is a must. Consistently good."</p>
      <div class="stars"><svg viewBox="0 0 14 14"><path d="M7 0l2 5h5l-4 3 2 6-5-4-5 4 2-6-4-3h5z" fill="var(--gold)"/></svg><svg viewBox="0 0 14 14"><path d="M7 0l2 5h5l-4 3 2 6-5-4-5 4 2-6-4-3h5z" fill="var(--gold)"/></svg><svg viewBox="0 0 14 14"><path d="M7 0l2 5h5l-4 3 2 6-5-4-5 4 2-6-4-3h5z" fill="var(--gold)"/></svg><svg viewBox="0 0 14 14"><path d="M7 0l2 5h5l-4 3 2 6-5-4-5 4 2-6-4-3h5z" fill="var(--gold)"/></svg></div>
      <div class="reviewer"><div class="avatar" role="img" aria-label="Reviewer portrait"></div><div><div class="reviewer-name">Dana Whitfield</div><div class="reviewer-place">Binghamton , New York</div></div></div>
    </article>

    <article class="review-card" style="left:829px">
      <div class="review-photo" role="img" aria-label="Photo of a plated side salad with a fork on a dark table" style="background:linear-gradient(135deg,#2b2b2b,#e8e6e0 45%,#b7c48a 75%,#3a3a3a)"></div>
      <div class="review-tag">Online Order</div>
      <p class="review-text">Ordered online and picked it up ten minutes later. Brisket was smoky and tender, sides were fresh. Consistently good."</p>
      <div class="stars"><svg viewBox="0 0 14 14"><path d="M7 0l2 5h5l-4 3 2 6-5-4-5 4 2-6-4-3h5z" fill="var(--gold)"/></svg><svg viewBox="0 0 14 14"><path d="M7 0l2 5h5l-4 3 2 6-5-4-5 4 2-6-4-3h5z" fill="var(--gold)"/></svg><svg viewBox="0 0 14 14"><path d="M7 0l2 5h5l-4 3 2 6-5-4-5 4 2-6-4-3h5z" fill="var(--gold)"/></svg><svg viewBox="0 0 14 14"><path d="M7 0l2 5h5l-4 3 2 6-5-4-5 4 2-6-4-3h5z" fill="var(--gold)"/></svg></div>
      <div class="reviewer"><div class="avatar" role="img" aria-label="Reviewer portrait"></div><div><div class="reviewer-name">Dana Whitfield</div><div class="reviewer-place">Binghamton , New York</div></div></div>
    </article>
  </section>

  <section class="browse">
    <h2 class="section-title">Browse<br>by Categories</h2>
    <div class="browse-rule"></div>

    <a class="category" style="left:63px;top:224px">
      <div class="photo" role="img" aria-label="Photo of smoked baby back ribs" style="background:linear-gradient(90deg,#6a4424,#b07a44 60%,#d8b27a)"></div>
      <svg class="band" viewBox="0 0 513 167"><polygon points="0,0 150,0 60,167 0,167" fill="var(--maroon-soft)"/></svg>
      <span class="icon"></span><span class="label">Ribs</span>
    </a>
    <a class="category" style="left:622px;top:224px">
      <div class="photo" role="img" aria-label="Photo of biscuits and gravy breakfast" style="background:linear-gradient(90deg,#f1ece6,#e3c28a 60%,#b97a3a)"></div>
      <svg class="band" viewBox="0 0 513 167"><polygon points="0,0 230,0 120,167 0,167" fill="var(--maroon-soft)"/></svg>
      <span class="icon"></span><span class="label">Breakfast</span>
    </a>
    <a class="category" style="left:63px;top:432px">
      <div class="photo" role="img" aria-label="Photo of collard greens and green bean sides" style="background:linear-gradient(90deg,#e9e6df,#7a9a4a 50%,#c24a3a)"></div>
      <svg class="band" viewBox="0 0 513 167"><polygon points="0,0 150,0 60,167 0,167" fill="var(--maroon-soft)"/></svg>
      <span class="icon"></span><span class="label">Sides</span>
    </a>
    <a class="category" style="left:622px;top:432px">
      <div class="photo" role="img" aria-label="Photo of sliced smoked brisket" style="background:linear-gradient(90deg,#8a5a2a,#e0963a 50%,#c76a28)"></div>
      <svg class="band" viewBox="0 0 513 167"><polygon points="0,0 230,0 120,167 0,167" fill="var(--maroon-soft)"/></svg>
      <span class="icon"></span><span class="label">Brisket</span>
    </a>
    <a class="category" style="left:63px;top:639px">
      <div class="photo" role="img" aria-label="Photo of a bowl of chili and cornbread" style="background:linear-gradient(90deg,#d8d2c4,#e6cf88 50%,#a88c5a)"></div>
      <svg class="band" viewBox="0 0 513 167"><polygon points="0,0 150,0 60,167 0,167" fill="var(--maroon-soft)"/></svg>
      <span class="icon"></span><span class="label">Soup</span>
    </a>
    <a class="category" style="left:622px;top:639px">
      <div class="photo" role="img" aria-label="Photo of peach cobbler with cream" style="background:linear-gradient(90deg,#f0e8e0,#e9d9b8 55%,#c8425a)"></div>
      <svg class="band" viewBox="0 0 513 167"><polygon points="0,0 230,0 120,167 0,167" fill="var(--maroon-soft)"/></svg>
      <span class="icon"></span><span class="label">Dessert</span>
    </a>
  </section>

  <footer class="footer">
    <span>COPYRIGHT © 2015 ORVANE . ALL RIGHTS RESERVED</span>
    <nav><span>DINE</span><span>SEARCH</span><span>WHO WE ARE</span><span>CONTACT</span></nav>
  </footer>

</div>
</body>
</html>
```